Solar Billboard Design

We require a billboard 24ftx10ft in size for our solar company.
Artwork Requirement’s:
• Sent on PDF file
• At least 300 dpi
• Scaled to 25% of banner size (24ft x 10ft)
• Please allow at least 40mm space from the artwork edge to allow for any hems and eyelets. This will ensure any important text/images are not cropped/overlapped.
The billboard must have on it:
Solar & Battery Packages
From £8750
In Stock Now!
brightfieldpower.co.uk (must stand out)
________________________
I have attached our logo and some images. I'm not sure if they are good enough quality so you may need to use a stock image.
Kind regards,
Marcus
Target Market(s)
Men & Women aged 35-70, homeowners
Industry/Entity Type
Solar / Construction
Look and feel
Each slider illustrates characteristics of the customer's brand and the style your logo design should communicate.

```html
<!DOCTYPE html>
<html lang="en">
<head>
<meta charset="utf-8">
<title>Brightfield Power Group – Solar &amp; Battery Billboard</title>
<link rel="stylesheet" href="https://fonts.googleapis.com/css2?family=Montserrat:wght@500;700;800&display=swap">
<style>
  :root {
    --page-bg: #c4c4c4;
    --brand-green: #2ecc5f;
    --ink-dark: #2f2f2f;
    --paper: #ffffff;
    --silver-light: #f2f2f2;
    --silver-mid: #b9b9b9;
    --carbon-dark: #141414;
    --carbon-mid: #262626;
    --rule-grey: #bdbdbd;
    --sky-top: #3f7fd8;
    --sky-low: #a9c8ee;
    --panel-dark: #1f2430;
    --roof-tile: #6b5a4c;
  }
  html, body {
    margin: 0;
    width: 1078px;
    height: 1200px;
    overflow: hidden;
    background: var(--page-bg);
  }
  .billboard {
    position: absolute;
    left: 39px;
    top: 392px;
    width: 1000px;
    height: 416px;
    box-shadow: 0 10px 22px rgba(0,0,0,0.35);
  }
  .billboard svg { display: block; width: 100%; height: 100%; }
  .headline, .price, .stock, .web, .brand-name {
    font-family: "Montserrat", sans-serif;
  }
  .brand-name { font-weight: 500; fill: var(--ink-dark); font-size: 29px; letter-spacing: 4px; }
  .headline { font-weight: 800; text-anchor: middle; }
  .headline-green { fill: var(--brand-green); font-size: 47px; }
  .headline-dark { fill: var(--ink-dark); font-size: 49px; }
  .price { font-weight: 700; fill: var(--paper); font-size: 30px; text-anchor: middle; }
  .stock { font-weight: 700; fill: var(--paper); font-size: 37px; text-anchor: middle; }
  .stock-accent { fill: var(--brand-green); }
  .web { font-weight: 700; fill: var(--brand-green); font-size: 23px; text-anchor: middle; }
  .web-tld { font-weight: 500; fill: var(--paper); }
  .web-rule { stroke: var(--rule-grey); stroke-width: 1.5; }
</style>
</head>
<body>
  <div class="billboard">
    <svg viewBox="0 0 1190 495" preserveAspectRatio="none" xmlns="http://www.w3.org/2000/svg">
      <defs>
        <linearGradient id="photoTone" x1="0" y1="0" x2="1" y2="1">
          <stop offset="0" stop-color="var(--roof-tile)"/>
          <stop offset="0.35" stop-color="var(--panel-dark)"/>
          <stop offset="0.6" stop-color="var(--sky-top)"/>
          <stop offset="1" stop-color="var(--sky-low)"/>
        </linearGradient>
        <linearGradient id="silverBand" x1="0" y1="0" x2="1" y2="0">
          <stop offset="0" stop-color="var(--silver-mid)"/>
          <stop offset="0.5" stop-color="var(--silver-light)"/>
          <stop offset="1" stop-color="var(--silver-mid)"/>
        </linearGradient>
        <linearGradient id="carbonBase" x1="0" y1="0" x2="1" y2="1">
          <stop offset="0" stop-color="var(--carbon-mid)"/>
          <stop offset="1" stop-color="var(--carbon-dark)"/>
        </linearGradient>
      </defs>

      <!-- panel backgrounds -->
      <rect class="paper" x="0" y="0" width="1190" height="495" fill="var(--paper)"/>
      <polygon class="silver-band" points="560,167 1190,167 1190,309 497,309" fill="url(#silverBand)"/>
      <polygon class="carbon-band" points="497,309 1190,309 1190,495 456,495" fill="url(#carbonBase)"/>

      <!-- photo area -->
      <polygon class="roof-photo" role="img" aria-label="Photo of black solar panels on a tiled house roof under a blue sky"
               points="0,0 606,0 446,495 0,495" fill="url(#photoTone)"/>

      <!-- diagonal green stripe -->
      <polygon class="accent-stripe" points="613,0 678,0 470,495 455,495" fill="var(--brand-green)"/>

      <!-- brand name -->
      <rect class="brand-mark" x="768" y="46" width="70" height="70" rx="4" fill="var(--brand-green)"/>
      <text class="brand-name" x="862" y="64">BRIGHTFIELD</text>
      <text class="brand-name" x="862" y="100">POWER</text>
      <text class="brand-name" x="862" y="136">GROUP</text>

      <!-- headline -->
      <text class="headline headline-green" x="888" y="227">SOLAR &amp; BATTERY</text>
      <text class="headline headline-dark" x="888" y="283">PACKAGES</text>

      <!-- price tag -->
      <polygon class="price-tag" points="740,310 1037,310 1005,362 770,362" fill="var(--brand-green)"/>
      <text class="price" x="888" y="346">From £8750</text>

      <!-- stock message -->
      <text class="stock" x="888" y="416">In Stock <tspan class="stock-accent">Now!</tspan></text>

      <!-- web address with divider broken around it -->
      <line class="web-rule" x1="482" y1="451" x2="718" y2="451"/>
      <line class="web-rule" x1="1042" y1="451" x2="1190" y2="451"/>
      <text class="web" x="880" y="459" textLength="296" lengthAdjust="spacingAndGlyphs">brightfieldpower<tspan class="web-tld">.co.uk</tspan></text>
    </svg>
  </div>
</body>
</html>
```